Business Card Design Project

Our slogan is "dare to be different" and we are after something creative and different to go with our company image.

Criteria:
The business card will not be a standard size but it must be small or big enough to fit in a wallet.
It will be double sided
It will have our colours and the design will be based around our logo (attached)
No fancy text just clean sharp easy to read. we have been using the stag sans book font type so this or similar type is preferable (we are not locked in a font type.

For more information about us, please visit out website at www.glimtrovale.com.au

Target Market(s)

outdoor and recreational industry/market

Industry/Entity Type

Business

Requirements
Must have
• Logo
Slogan
website
contact details (phone and email)
Name and Position
social media facebook and youtube

```html
<!DOCTYPE html>
<html lang="en">
<head>
<meta charset="utf-8">
<title>Glimtrovale Business Card</title>
<link href="https://fonts.googleapis.com/css2?family=Montserrat:wght@400;600;700&family=Tinos:wght@400;700&display=swap" rel="stylesheet">
<style>
  :root {
    --page: #e9e6e1;
    --card-black: #0d0d0d;
    --card-grey: #2b2b2b;
    --card-grey-light: #3c3c3c;
    --red: #e8240c;
    --red-deep: #9e1707;
    --white: #f4f4f4;
    --muted: #b9b9b9;
  }
  * { box-sizing: border-box; margin: 0; padding: 0; }
  html, body { width: 1200px; height: 900px; overflow: hidden; }
  body {
    background: var(--page);
    font-family: "Montserrat", sans-serif;
    display: flex;
    flex-direction: column;
    align-items: center;
    justify-content: center;
    gap: 44px;
  }
  .card {
    position: relative;
    width: 680px;
    height: 380px;
    border-radius: 4px;
    overflow: hidden;
    box-shadow: 0 10px 28px rgba(0,0,0,.28);
  }
  .card-art { position: absolute; inset: 0; }

  /* Front */
  .brand { position: absolute; left: 34px; top: 62px; display: flex; align-items: center; gap: 16px; }
  .brand-dot { width: 76px; height: 76px; border-radius: 50%; border: 5px solid var(--red); }
  .brand-name { font-weight: 600; font-size: 30px; color: var(--white); letter-spacing: 1px; text-transform: uppercase; }
  .slogan-front { position: absolute; left: 128px; top: 122px; font-size: 11px; font-weight: 600; color: var(--white); letter-spacing: 2px; text-transform: uppercase; }
  .person { position: absolute; left: 420px; top: 78px; }
  .person-name { font-weight: 700; font-size: 27px; color: var(--white); text-transform: uppercase; }
  .person-name .surname { color: var(--red); }
  .person-role { font-family: "Tinos", serif; font-size: 15px; color: var(--muted); letter-spacing: 1px; text-transform: uppercase; margin-top: 2px; }
  .address { position: absolute; left: 420px; top: 150px; font-family: "Tinos", serif; font-size: 15px; line-height: 1.2; color: var(--red); }
  .contact-row { position: absolute; left: 28px; right: 28px; display: flex; justify-content: space-between; font-family: "Tinos", serif; font-size: 14px; letter-spacing: .5px; }
  .contact-row.social { top: 290px; color: var(--muted); font-variant: small-caps; }
  .contact-row.web { top: 328px; color: var(--red); font-weight: 700; text-transform: uppercase; }
  .contact { display: flex; align-items: center; gap: 8px; }
  .mark { width: 12px; height: 12px; background: var(--red); }

  /* Back */
  .card-back { background: var(--card-black); }
  .back-dot { position: absolute; left: 296px; top: 60px; width: 88px; height: 88px; border-radius: 50%; border: 5px solid var(--red); }
  .back-name { position: absolute; top: 166px; width: 100%; text-align: center; font-weight: 600; font-size: 38px; color: var(--white); letter-spacing: 2px; text-transform: uppercase; }
  .back-region { position: absolute; top: 222px; width: 100%; text-align: center; font-size: 13px; color: var(--white); letter-spacing: 10px; text-transform: uppercase; }
  .back-slogan { position: absolute; top: 262px; width: 100%; text-align: center; font-size: 14px; color: var(--red); letter-spacing: 6px; text-transform: uppercase; }
  .back-web { position: absolute; top: 306px; width: 100%; text-align: center; font-size: 13px; font-weight: 700; color: var(--white); text-transform: uppercase; letter-spacing: .5px; }
</style>
</head>
<body>

<section class="card card-front">
  <svg class="card-art" viewBox="0 0 680 380" aria-hidden="true">
    <defs>
      <linearGradient id="greyFade" x1="0" y1="0" x2="1" y2="1">
        <stop offset="0" stop-color="#3c3c3c"/>
        <stop offset="1" stop-color="#232323"/>
      </linearGradient>
    </defs>
    <rect width="680" height="380" fill="url(#greyFade)"/>
    <polygon points="0,0 680,0 680,258 470,258 440,236 290,236 258,268 0,268" fill="#0d0d0d"/>
    <polyline points="0,268 258,268 290,236 440,236 470,258 680,258" fill="none" stroke="#9e1707" stroke-width="4"/>
    <polygon points="0,40 150,40 190,8 330,8 350,0 400,0 360,30 210,30 170,62 20,62 0,82" fill="#e8240c"/>
    <polygon points="0,190 25,170 25,230 0,250" fill="#e8240c"/>
    <polygon points="370,50 680,50 680,60 380,60 350,150 340,150" fill="#9e1707"/>
  </svg>

  <div class="brand">
    <span class="brand-dot"></span>
    <span class="brand-name">Glimtrovale</span>
  </div>
  <p class="slogan-front">Dare to be different</p>

  <div class="person">
    <p class="person-name">Alex <span class="surname">Marlow</span></p>
    <p class="person-role">Head of Operations</p>
  </div>
  <p class="address">Unit 12, 48 Kestrel Lane<br>Wattle Grove, Brisbane,<br>Queensland, Australia 4109<br>(+61) 555 010 482</p>

  <div class="contact-row social">
    <span class="contact"><span class="mark"></span>@TheGlimtrovale</span>
    <span class="contact"><span class="mark"></span>@Glimtrovale/info</span>
  </div>
  <div class="contact-row web">
    <span class="contact"><span class="mark"></span>enquiries@glimtrovale.com.au</span>
    <span class="contact"><span class="mark"></span>www.glimtrovale.com.au</span>
  </div>
</section>

<section class="card card-back">
  <span class="back-dot"></span>
  <p class="back-name">Glimtrovale</p>
  <p class="back-region">Australia</p>
  <p class="back-slogan">Dare to be different</p>
  <p class="back-web">www.glimtrovale.com.au</p>
</section>

</body>
</html>
```